Would like a Northwest feel to the look, something NOT typical of what you would see on a typical Home Inspectors logo. Real estate cards all the same as well, and would like to stand out. Earthy, green, Northwest. Sadly a portrait seems to be a requirement (see the attached). I inspect residential homes for buyers and sellers.

Target Market(s)

Home Buyers and Sellers

Industry/Entity Type

Home Inspection

Contact Information for Business Card

See description
Note: The name Corvaneth is a Chinook word that means 'Friend'. Please do not associate the name with the Whale that shows up on 99% of google searches.

Logo Text

Corvaneth Home Inspections

Colors

Designer to choose colors to be used in the design.

Requirements
Must have
• Phone Num: 541-672-8153
• Address: 732 SW 219th Av Num 618
• Portland, Oregon 97388
• Email: glen@corvanethhomeinspection.example
• Website: www.CorvanethHomeInspection.example
• Additional Note: Need to add the Obravex logo (icon). It should be small and not the focus of the card. The logo can be found at Obravex.example
Nice to have
• I am open
Should not have
• Cant think of anything

```html
<!DOCTYPE html>
<html lang="en">
<head>
<meta charset="utf-8">
<title>Corvaneth Home Inspections – Business Card</title>
<link rel="stylesheet" href="https://fonts.googleapis.com/css2?family=Montserrat:wght@300;400;500&display=swap">
<style>
  :root {
    --page: #2b2b2c;
    --forest: #34432f;
    --band-forest: #3f4d3a;
    --white: #ffffff;
    --cream: #f6f3ea;
    --ochre: #c4913a;
    --moss: #6f8f4a;
    --logo-green: #3e6a3a;
    --sub-brown: #7a5a3a;
    --photo-top: #b9a694;
    --photo-bottom: #7d7f6a;
  }
  * { box-sizing: border-box; margin: 0; padding: 0; }
  html, body { width: 1200px; height: 880px; overflow: hidden; }
  body {
    background: var(--page);
    font-family: "Montserrat", Arial, sans-serif;
    position: relative;
  }
  .card {
    position: absolute;
    width: 560px;
    height: 320px;
    border-radius: 22px;
    overflow: hidden;
  }
  .brand {
    position: absolute;
    display: flex;
    align-items: center;
    gap: 14px;
  }
  .brand-dot {
    width: 54px; height: 54px;
    border-radius: 50%;
    flex: none;
  }
  .brand-name {
    font-weight: 300;
    font-size: 40px;
    letter-spacing: 3px;
    text-transform: uppercase;
    line-height: 1;
  }
  .brand-sub {
    font-weight: 300;
    font-size: 24px;
    letter-spacing: 1.5px;
    margin-top: 4px;
    line-height: 1;
  }

  /* Back side */
  .card-back {
    left: 60px; top: 90px;
    background: var(--forest);
    color: var(--cream);
  }
  .card-back .brand { left: 110px; top: 96px; }
  .card-back .brand-dot { border: 2px solid var(--cream); }
  .back-address {
    position: absolute;
    left: 0; right: 0; bottom: 52px;
    text-align: center;
    font-size: 14px;
    font-weight: 400;
    letter-spacing: 0.3px;
  }

  /* Front side */
  .card-front {
    left: 580px; top: 470px;
    background: var(--white);
  }
  .front-bands { position: absolute; inset: 0; }
  .portrait {
    position: absolute;
    right: 0; top: 18px;
    width: 180px; height: 256px;
    background: linear-gradient(180deg, var(--photo-top), var(--photo-bottom));
    border-radius: 40px 0 0 0;
  }
  .card-front .brand { left: 28px; top: 40px; color: var(--logo-green); }
  .card-front .brand-dot { background: var(--moss); width: 46px; height: 46px; }
  .card-front .brand-name { font-size: 32px; }
  .card-front .brand-sub { font-size: 20px; color: var(--logo-green); }
  .contact {
    position: absolute;
    left: 60px; top: 180px;
    color: var(--white);
  }
  .employee-name {
    font-size: 19px;
    font-weight: 500;
    letter-spacing: 0.5px;
    text-transform: uppercase;
    margin-bottom: 8px;
  }
  .contact-line {
    font-size: 13px;
    font-weight: 400;
    line-height: 1.45;
  }
  .partner-badge {
    position: absolute;
    left: 318px; top: 180px;
    width: 30px; height: 30px;
    border-radius: 50%;
    background: var(--cream);
    border: 3px solid var(--ochre);
  }
  .website {
    position: absolute;
    left: 100px; bottom: 11px;
    color: var(--white);
    font-size: 14px;
    font-weight: 400;
    letter-spacing: 0.3px;
  }
</style>
</head>
<body>

  <section class="card card-back" aria-label="Business card back">
    <div class="brand">
      <span class="brand-dot"></span>
      <div>
        <div class="brand-name">Corvaneth</div>
        <div class="brand-sub">Home Inspections</div>
      </div>
    </div>
    <p class="back-address">732 SW 219th Av Num 618 Portland, Oregon 97388</p>
  </section>

  <section class="card card-front" aria-label="Business card front">
    <svg class="front-bands" width="560" height="320" viewBox="0 0 560 320" aria-hidden="true">
      <polygon points="0,172 560,118 560,320 0,320" fill="var(--band-forest)"/>
      <polygon points="0,168 560,114 560,120 0,174" fill="var(--ochre)"/>
      <polygon points="0,286 560,258 560,320 0,320" fill="var(--moss)"/>
    </svg>
    <div class="portrait" role="img" aria-label="Portrait photo of the inspector"></div>
    <div class="brand">
      <span class="brand-dot"></span>
      <div>
        <div class="brand-name">Corvaneth</div>
        <div class="brand-sub">Home Inspections</div>
      </div>
    </div>
    <div class="contact">
      <div class="employee-name">Employee Name</div>
      <div class="contact-line">541-672-8153</div>
      <div class="contact-line">glen@corvanethhomeinspection.example</div>
    </div>
    <span class="partner-badge" role="img" aria-label="Obravex member badge"></span>
    <div class="website">www.CORVANETHHOMEINSPECTION.example</div>
  </section>

</body>
</html>
```